Design Startseite Kanzlei-Homepage
Zielgruppe
Wir sind eine Rechtsanwaltskanzlei in Kempten (Allgäu) und regional sowie überregional in verschiedenen Rechtsgebieten tätig. Unsere Zielgruppe sind sowohl private als auch gewerbliche Mandanten.
Aufgabenstellung
Die bestehende Gestaltung wirkt derzeit aus unserer Sicht überholt. Insbesondere soll das bislang dominierende Rot vollständig entfallen.
Stattdessen stellen wir uns ein modernes, hochwertiges Erscheinungsbild vor, primär in dunklen Farbtönen (Anthrazit/Schwarz) kombiniert mit Beige- bzw. warmen Naturtönen. Ziel ist eine klare visuelle Anlehnung an unsere Kanzleiräumlichkeiten (siehe Fotos).
Die Webseite soll insgesamt moderner, klarer und visuell anspruchsvoller wirken, ohne an Seriosität und Zugänglichkeit einzubüßen. Die Balance zwischen hochwertigem Erscheinungsbild und mandantenorientierter Nutzerführung steht für uns im Vordergrund.

```html
<!DOCTYPE html>
<html lang="de">
<head>
<meta charset="utf-8">
<title>Lindenhof Rechtsanwälte – Startseite</title>
<link href="https://fonts.googleapis.com/css2?family=Outfit:wght@300;400;500;600&display=swap" rel="stylesheet">
<style>
  :root{
    --anthracite:#2a2a2c;
    --gold:#c2a371;
    --cream:#f3efe7;
    --ink:#1e1e1e;
    --text-muted:#5a5750;
    --white:#ffffff;
  }
  *{margin:0;padding:0;box-sizing:border-box}
  html,body{width:1200px;height:2453px;overflow:hidden;background:var(--anthracite)}
  body{font-family:"Outfit",sans-serif;color:var(--white);position:relative}
  .hero{position:absolute;left:0;top:0;width:1200px;height:602px;
    background:radial-gradient(ellipse at 45% 45%,#5a4f3f 0%,#3a3630 35%,#23262f 75%,#1c1e26 100%)}
  .hero__shade{position:absolute;inset:0;background:linear-gradient(180deg,rgba(28,30,40,.55) 0%,rgba(20,20,24,.2) 50%,rgba(20,20,22,.75) 100%)}
  .brand{position:absolute;left:145px;top:29px;font-weight:500;font-size:18px;line-height:20px;color:var(--white)}
  .nav{position:absolute;right:143px;top:24px;display:flex;align-items:center;gap:23px;font-size:12px;font-weight:500}
  .nav__chat{width:31px;height:31px;border-radius:50%;background:var(--gold);display:flex;align-items:center;justify-content:center}
  .hero__badge{position:absolute;left:576px;top:121px;width:46px;height:46px;border-radius:50%;background:#f1ede6;display:flex;align-items:center;justify-content:center}
  .hero__title{position:absolute;left:0;top:192px;width:1200px;text-align:center;font-weight:500;font-size:54px;line-height:75px;letter-spacing:.5px}
  .hero__title em{font-style:normal;color:var(--gold)}
  .btn{position:absolute;display:flex;align-items:center;justify-content:center;font-size:10.5px;font-weight:500}
  .btn--gold{left:523px;top:441px;width:153px;height:36px;background:var(--gold);color:var(--ink)}
  .stats{position:absolute;left:0;top:602px;width:1200px;height:104px;background:var(--anthracite)}
  .stat{position:absolute;top:26px;width:200px;margin-left:-100px;text-align:center}
  .stat__num{font-size:23px;font-weight:300;color:var(--gold);line-height:26px}
  .stat__label{font-size:9px;color:#b8b3aa;margin-top:2px}
  .about{position:absolute;left:0;top:706px;width:1200px;height:800px;background:var(--cream)}
  .about__photo{position:absolute;left:600px;top:0;width:600px;height:800px;
    background:linear-gradient(90deg,var(--cream) 0%,#dedbd4 18%,#cfcdc8 40%,#8f8b84 70%,#a48a66 100%)}
  .about__text{position:absolute;left:142px;top:158px;width:312px;color:var(--ink)}
  .eyebrow{font-size:8px;font-weight:600;letter-spacing:1.5px;color:var(--gold)}
  .about__title{font-size:28px;font-weight:500;line-height:29px;margin-top:12px}
  .about__body{font-size:12px;letter-spacing:.4px;line-height:18.6px;color:var(--text-muted);margin-top:20px}
  .about__body + .about__body{margin-top:11px}
  .btn--dark{position:relative;margin-top:22px;width:152px;height:32px;background:var(--ink);color:var(--white)}
  .team{position:absolute;left:0;top:1506px;width:1200px;height:801px;
    background:radial-gradient(ellipse at 50% 40%,#4a4a4c 0%,#3b3b3d 50%,#323234 100%)}
  .team__claim{position:absolute;left:0;top:316px;width:1200px;text-align:center;font-weight:300;font-size:49px;line-height:63px}
  .team__rule{position:absolute;left:550px;top:480px;width:100px;height:3px;background:var(--gold)}
  .footer-band{position:absolute;left:0;top:2307px;width:1200px;height:146px;background:linear-gradient(180deg,#2a2a2c 0%,#3c3c3e 100%)}
</style>
</head>
<body>
  <header class="hero">
    <div class="hero__bg" role="img" aria-label="Abendfoto des Kanzleigebäudes mit beleuchteten Fenstern und Bäumen" style="position:absolute;inset:0"></div>
    <div class="hero__shade"></div>
    <div class="brand">Lindenhof Rechtsanwälte</div>
    <nav class="nav">
      <span>Startseite</span><span>Über uns</span><span>Rechtsgebiete</span><span>Team</span>
      <span class="nav__chat">
        <svg width="15" height="15" viewBox="0 0 16 16" fill="none" stroke="#2a2a2c" stroke-width="1.5"><path d="M8 2a6 6 0 1 0 3 11.2L14 14l-.8-3A6 6 0 0 0 8 2z"/><path d="M5.5 7h5M5.5 9.5h3"/></svg>
      </span>
    </nav>
    <div class="hero__badge">
      <svg width="20" height="20" viewBox="0 0 20 20" fill="none" stroke="#2a2a2c" stroke-width="1.4"><path d="M10 3v13M6 16h8M4 6h12"/><path d="M4 6l-2.5 5h5zM16 6l-2.5 5h5z"/></svg>
    </div>
    <h1 class="hero__title">Ihre Rechtsanwälte<br>im Herzen des<br><em>Allgäus</em></h1>
    <a class="btn btn--gold">Kontakt aufnehmen</a>
  </header>

  <section class="stats">
    <div class="stat" style="left:310px"><div class="stat__num">7</div><div class="stat__label">Rechtsgebiete</div></div>
    <div class="stat" style="left:599px"><div class="stat__num">7</div><div class="stat__label">Rechtsanwälte</div></div>
    <div class="stat" style="left:888px"><div class="stat__num">25+</div><div class="stat__label">Jahre Erfahrung</div></div>
  </section>

  <section class="about">
    <div class="about__photo" role="img" aria-label="Heller Flur der Kanzleiräume mit Holzverkleidung und Garderobe"></div>
    <div class="about__text">
      <div class="eyebrow">ÜBER UNS</div>
      <h2 class="about__title">Persönlich. Kompetent.<br>Verlässlich.</h2>
      <p class="about__body">Die Mitglieder unseres Anwaltsteams – jeweils ergänzt um ein ansprechend eingerichtetes und funktional ausgestattetes Sekretariat – spezialisieren sich in unterschiedliche Fachrichtungen, sodass für Sie eine große Bandbreite in der mandantenorientierten Rechtsberatung sichergestellt ist. Das gilt insbesondere für unsere Schwerpunkte im Verkehrsrecht und Strafrecht sowie im Arbeitsrecht, Erbrecht, Mietrecht, Baurecht und Familienrecht.</p>
      <p class="about__body">Auf die Mandatierung externer Anwälte kann durch die thematische Vielfalt und Spezialisierung unserer Juristen in den meisten Fällen verzichtet werden. Gleichzeitig gewährleistet unser engagiertes Kanzleiteam eine rechtliche Unterstützung ganz nach Ihren individuellen Interessen, stets auf dem neuesten Stand von Rechtsprechung und Praxis – seit mehr als 25 Jahren.</p>
      <a class="btn btn--dark">Kontakt aufnehmen</a>
    </div>
  </section>

  <section class="team">
    <div role="img" aria-label="Gruppenfoto des Kanzleiteams auf gepflastertem Platz" style="position:absolute;inset:0"></div>
    <p class="team__claim">Kompetenz,<br>die Vertrauen schafft.</p>
    <div class="team__rule"></div>
  </section>

  <div class="footer-band"></div>
</body>
</html>
```